Brightleaf Card Venture Flyer

I need a DL sized flyer that will be sent out to participants in our Brightleaf Card Venture - sharing 1million Brightleaf Cards with the world. This flyer will form the first tangible item most of our community will receive from Lifting the Horizon, so it needs to be able to communicate our goal of inspiring change, possibility, kindness and love in the world.

Target Market(s)

Women aged 30 - 50, sophisticated, generous, philanthropy minded, contemporary, elegant

Font styles to use
Sans Serif
Other font styles liked:
• Raleway

Colors

Designer to choose colors to be used in the design.

Requirements
Must have
• Must be DL size - i.e. one third of an A4. On one side the flyer must also include space for the Brightleaf Cards to be stuck - the brightleaf cards are Stikkas that are 3in (76mm) square.
• The logo must be included somewhere, along with the website and social media icons - liftingthehorizon.com.au, Facebook, Instagram, Twitter all @liftingthehorizon.
• The copy for the flyer is:
• Thank you so much for helping us to reach our goal of having one million brightleaf cards out in the world. Share one of our notes with a friend, a family member, with a total stranger, or perhaps just with yourself. And remember that you might just be Lifting the Horizon in someone else's day.
• Share the story of your brightleaf cards on social media with the hashtag #brightleafcardventure or send us a photo and your story to bcventure@liftingthehorizon.com.au

```html
<!DOCTYPE html>
<html lang="en">
<head>
<meta charset="utf-8">
<title>Brightleaf Card Venture Flyer</title>
<link rel="stylesheet" href="https://fonts.googleapis.com/css2?family=Bebas+Neue&family=Comfortaa:wght@600;700&family=Raleway:wght@400;600&display=swap">
<style>
  :root {
    --backdrop: #cfd2ee;
    --paper: #f2f2f2;
    --ink: #3a3a3a;
    --white: #ffffff;
    --teal: #1f7a72;
    --note-grey: #b0b0b0;
    --wash-pink: #e9a9c6;
    --wash-blue: #a6bde3;
    --wash-peach: #eeb99c;
    --wash-lilac: #c9b2e0;
    --text-shadow: 0 1px 2px rgba(0,0,0,.75), 0 0 6px rgba(0,0,0,.35);
  }
  * { box-sizing: border-box; margin: 0; padding: 0; }
  html, body { width: 1200px; height: 1000px; overflow: hidden; }
  body { background: var(--backdrop); position: relative; font-family: "Bebas Neue", sans-serif; }

  .flyer { position: absolute; background: var(--paper); box-shadow: 6px 10px 18px rgba(60,60,110,.35); overflow: hidden; }
  .flyer--front { left: 180px; top: 55px; width: 390px; height: 890px; }
  .flyer--back { left: 723px; top: 55px; width: 375px; height: 890px; }

  .wash { position: absolute; }
  .wash--strip { left: 190px; top: 0; width: 200px; height: 890px;
    background: linear-gradient(180deg, var(--wash-blue) 0%, #c9d5ec 30%, var(--wash-lilac) 50%, var(--wash-peach) 62%, var(--wash-pink) 80%, #e2a0c0 100%); }

  .emblem-ring { position: absolute; left: 55px; top: 77px; width: 270px; height: 270px; border-radius: 50%; background: var(--white); }
  .emblem-ring::before { content: ""; position: absolute; inset: 14px; border-radius: 50%;
    border: 9px solid transparent;
    background: conic-gradient(var(--wash-pink), var(--wash-peach), #f2b07a, var(--wash-blue), var(--wash-lilac), var(--wash-pink)) border-box;
    -webkit-mask: linear-gradient(#000 0 0) padding-box, linear-gradient(#000 0 0);
    -webkit-mask-composite: xor; mask-composite: exclude; }
  .emblem-name { position: absolute; left: 0; right: 0; top: 108px; text-align: center;
    font-family: "Raleway", sans-serif; font-weight: 600; font-size: 26px; line-height: 1.15; color: var(--teal); }

  .title-frame { position: absolute; left: 0; top: 0; }
  .title-part { position: absolute; font-size: 42px; line-height: 1; letter-spacing: .5px; }
  .title-part--lead { left: 203px; top: 392px; color: var(--white); text-shadow: var(--text-shadow); }
  .title-part--small { right: 205px; top: 372px; font-size: 22px; color: var(--ink); }
  .title-part--tail { right: 205px; top: 394px; font-size: 38px; color: var(--ink); }

  .copy { position: absolute; left: 32px; width: 335px; color: var(--white); font-size: 19px; line-height: 25px; text-shadow: var(--text-shadow); }
  .copy--intro { top: 490px; }
  .copy--list { top: 578px; list-style: none; }
  .copy--list li { position: relative; padding-left: 22px; height: 25px; }
  .copy--list li::before { content: ""; position: absolute; left: 0; top: 5px; width: 12px; height: 12px; border-radius: 50%; background: var(--teal); }
  .copy--outro { top: 694px; }

  .handle { position: absolute; left: 0; right: 0; top: 783px; text-align: center; font-size: 15px; color: var(--white); text-shadow: var(--text-shadow); }
  .site { position: absolute; left: 0; right: 0; top: 870px; text-align: center; font-size: 13px; color: var(--white); text-shadow: var(--text-shadow); }
  .social-dot { position: absolute; top: 817px; width: 42px; height: 42px; border-radius: 50%; border: 2px solid var(--white);
    background: rgba(255,255,255,.35); box-shadow: 0 1px 3px rgba(0,0,0,.35); }

  .band { position: absolute; left: 0; width: 375px; }
  .band--masthead { top: 0; height: 180px;
    background: linear-gradient(100deg, var(--wash-pink) 0%, #f3cfdd 35%, var(--wash-peach) 60%, var(--wash-pink) 100%); }
  .band--hashtag { top: 360px; height: 56px;
    background: linear-gradient(90deg, var(--wash-pink), var(--wash-blue) 45%, var(--wash-peach) 70%, var(--wash-blue)); }
  .band--email { top: 517px; height: 60px;
    background: linear-gradient(90deg, var(--wash-pink), var(--wash-lilac) 40%, var(--wash-blue) 70%, var(--wash-pink)); }

  .masthead { position: absolute; left: 0; right: 0; top: 32px; text-align: center; font-family: "Raleway", sans-serif;
    color: var(--white); text-shadow: 0 2px 4px rgba(0,0,0,.35); }
  .masthead__top { font-size: 36px; font-weight: 400; line-height: 1; }
  .masthead__bottom { font-size: 48px; font-weight: 600; line-height: 1.2; color: var(--ink); text-shadow: 0 2px 4px rgba(0,0,0,.25); }

  .prompt { position: absolute; left: 0; right: 0; text-align: center; font-family: "Comfortaa", sans-serif; font-weight: 700;
    color: var(--ink); font-size: 24px; line-height: 32px; text-shadow: 0 2px 3px rgba(0,0,0,.2); }
  .prompt--share { top: 206px; }
  .prompt--send { top: 442px; }
  .hashtag { position: absolute; left: 0; right: 0; top: 370px; text-align: center; font-family: "Comfortaa", sans-serif; font-weight: 600;
    font-size: 25px; color: var(--ink); }
  .email { position: absolute; left: 0; right: 0; top: 536px; text-align: center; font-family: "Comfortaa", sans-serif; font-weight: 600;
    font-size: 16px; color: var(--ink); }

  .note-space { position: absolute; left: 25px; top: 638px; width: 329px; height: 237px; background: var(--note-grey); }
  .note-tab { position: absolute; left: 274px; top: 595px; width: 85px; height: 85px; background: var(--paper); }
  .note-label { position: absolute; right: 20px; top: 595px; text-align: right; font-size: 38px; line-height: 34px; color: var(--white);
    text-shadow: var(--text-shadow); }
  .note-line { position: absolute; height: 1px; background: var(--white); left: 43px; }
</style>
</head>
<body>

<section class="flyer flyer--front">
  <div class="wash wash--strip" role="img" aria-label="Soft pastel watercolour wash in blue, lilac, peach and pink"></div>

  <div class="emblem-ring">
    <p class="emblem-name">Lifting<br>the Horizon</p>
  </div>

  <svg class="title-frame" width="390" height="890" viewBox="0 0 390 890" aria-hidden="true">
    <g fill="none" stroke="#ffffff" stroke-width="3">
      <polyline points="30,437 193,437 193,367 342,367"/>
      <polyline points="10,806 110,806 110,862 270,862 270,806 380,806"/>
    </g>
  </svg>
  <h1>
    <span class="title-part title-part--small">The</span>
    <span class="title-part title-part--tail">Horizon</span>
    <span class="title-part title-part--lead">Lifting</span>
  </h1>

  <p class="copy copy--intro">Thank you so much for helping us to reach our goal of having one million brightleaf cards out in the world.</p>
  <ul class="copy copy--list">
    <li>Share one of our notes with a friend,</li>
    <li>a family member,</li>
    <li>with a total stranger,</li>
    <li>or perhaps just with yourself.</li>
  </ul>
  <p class="copy copy--outro">And remember that you might just be Lifting the Horizon in someone else's day.</p>

  <p class="handle">@liftingthehorizon</p>
  <span class="social-dot" style="left:30px" aria-label="Social profile"></span>
  <span class="social-dot" style="left:168px" aria-label="Social profile"></span>
  <span class="social-dot" style="left:308px" aria-label="Social profile"></span>
  <p class="site">www.liftingthehorizon.com.au</p>
</section>

<section class="flyer flyer--back">
  <div class="band band--masthead" role="img" aria-label="Pink and peach watercolour wash"></div>
  <h2 class="masthead"><span class="masthead__top">lifting the</span><br><span class="masthead__bottom">horizon</span></h2>

  <p class="prompt prompt--share">Share the story of your<br>brightleaf cards on<br>social media with<br>the hashtag</p>

  <div class="band band--hashtag" role="img" aria-label="Pastel watercolour band"></div>
  <p class="hashtag">#brightleafcardventure</p>

  <p class="prompt prompt--send">or send us a photo and<br>your story to</p>

  <div class="band band--email" role="img" aria-label="Pastel watercolour band"></div>
  <p class="email">bcventure@liftingthehorizon.com.au</p>

  <div class="note-space"></div>
  <div class="note-tab"></div>
  <p class="note-label">Brightleaf<br>Card</p>
  <span class="note-line" style="top:679px;width:200px"></span>
  <span class="note-line" style="top:715px;width:290px"></span>
  <span class="note-line" style="top:750px;width:290px"></span>
  <span class="note-line" style="top:786px;width:290px"></span>
  <span class="note-line" style="top:822px;width:290px"></span>
  <span class="note-line" style="top:858px;width:290px"></span>
</section>

</body>
</html>
```